Business cards Dorn Kelterhof GmbH & Co.KG

We need a uniform business card design template for our employees.
A template should be created to have the same design for all business cards.

Contact Information for Business Card

Firma und Firmierung, Name, Funktion in Unternehmen, Anschrift, Tel. Handynummer, Emailadresse, Internetseite

Colors

Designer to choose colors to be used in the design.

Requirements
Must have
• Our company logo must be on it

```html
<!DOCTYPE html>
<html lang="de">
<head>
<meta charset="utf-8">
<title>Dorn Kelterhof – Visitenkarten</title>
<link rel="stylesheet" href="https://fonts.googleapis.com/css2?family=Libre+Baskerville:wght@400;700&family=Arimo:wght@400&display=swap">
<style>
  :root {
    --backdrop: #2a2a2c;
    --card: #141414;
    --lilac: #c9a2d9;
    --rose: #f27b8c;
    --serif: "Libre Baskerville", "Times New Roman", serif;
    --sans: "Arimo", Arial, sans-serif;
  }
  * { box-sizing: border-box; margin: 0; padding: 0; }
  html, body { width: 1200px; height: 1200px; overflow: hidden; }
  body {
    background: var(--backdrop);
    position: relative;
    font-family: var(--sans);
  }
  .card {
    position: absolute;
    left: 150px;
    width: 900px;
    height: 500px;
    background: var(--card);
    box-shadow: 0 10px 30px rgba(0,0,0,.45);
  }
  .card--front { top: 80px; }
  .card--back { top: 620px; }

  .brand-name {
    position: absolute;
    font-family: var(--serif);
    font-weight: 400;
    color: var(--rose);
    letter-spacing: 1px;
    white-space: nowrap;
  }
  .card--front .brand-name {
    left: 0; right: 0; top: 210px;
    text-align: center;
    font-size: 56px;
  }
  .card--back .brand-name {
    right: 60px; top: 140px;
    font-size: 42px;
  }

  .holder {
    position: absolute;
    left: 90px; top: 70px;
  }
  .holder__name {
    font-family: var(--serif);
    font-weight: 700;
    color: var(--rose);
    font-size: 32px;
  }
  .holder__role {
    color: var(--lilac);
    font-size: 22px;
    margin-top: 4px;
  }

  .rule {
    position: absolute;
    top: 310px;
    height: 2px;
  }
  .rule--contact { left: 90px; width: 460px; background: var(--lilac); }
  .rule--address { left: 600px; width: 240px; background: var(--rose); }

  .contact {
    position: absolute;
    left: 90px; top: 335px;
    list-style: none;
  }
  .contact li {
    display: flex;
    align-items: center;
    gap: 14px;
    color: var(--rose);
    font-size: 22px;
    line-height: 34px;
  }
  .contact svg { width: 22px; height: 22px; flex: none; }

  .address {
    position: absolute;
    right: 60px; top: 335px;
    text-align: right;
    font-style: normal;
    color: var(--rose);
    font-size: 22px;
    line-height: 32px;
  }
</style>
</head>
<body>

<section class="card card--front" aria-label="Vorderseite">
  <p class="brand-name">Dorn Kelterhof</p>
</section>

<section class="card card--back" aria-label="Rückseite">
  <div class="holder">
    <p class="holder__name">Lena Marwitz</p>
    <p class="holder__role">Managing Director</p>
  </div>

  <p class="brand-name">Dorn Kelterhof</p>

  <div class="rule rule--contact"></div>
  <div class="rule rule--address"></div>

  <ul class="contact">
    <li>
      <svg viewBox="0 0 24 24" aria-hidden="true"><path fill="var(--lilac)" d="M6.6 10.8a15.1 15.1 0 0 0 6.6 6.6l2.2-2.2a1 1 0 0 1 1-.25 11.4 11.4 0 0 0 3.6.57 1 1 0 0 1 1 1V20a1 1 0 0 1-1 1A17 17 0 0 1 3 4a1 1 0 0 1 1-1h3.5a1 1 0 0 1 1 1c0 1.25.2 2.45.57 3.57a1 1 0 0 1-.25 1z"/></svg>
      214-555-0187
    </li>
    <li>
      <svg viewBox="0 0 24 24" aria-hidden="true"><rect x="2" y="5" width="20" height="14" fill="none" stroke="var(--lilac)" stroke-width="2"/><path d="M2 5l10 8 10-8" fill="none" stroke="var(--lilac)" stroke-width="2"/></svg>
      lena@mailbox-example.com
    </li>
    <li>
      <svg viewBox="0 0 24 24" aria-hidden="true" fill="none" stroke="var(--lilac)" stroke-width="1.8"><circle cx="12" cy="12" r="10"/><ellipse cx="12" cy="12" rx="4.5" ry="10"/><path d="M2 12h20M4 7h16M4 17h16"/></svg>
      www.dornkelterhof.com
    </li>
  </ul>

  <address class="address">
    118 Harlow Street NE<br>
    Suite 210, Millbrook<br>
    MI 49620
  </address>
</section>

</body>
</html>
```